MARLOWE BRIGHT WORKS WEBSITE HOME PAGE AND CHECKOUT PAGES

UPDATE TO BRIEF:

Marlowe Bright Works is a company that provides Charities with the Free Vacation Vouchers that they can use to incentivize people to donate which in turn increases donations for the chairty.

So I need to keep it a little more template like the example url I gave. http://pagefernly.com/marlowe-bright-work/ Because, I am going to provide template to ANY CHARITY TYPE and they just fill in the content into the template and change images or whatever for their charity. So I am really looking for a website template that can be used for multiple and different kinds of charities.

So where the logo would go please use YOUR LOGO HERE generic logo for now

and where ever you promote the Free Vacation Certificate To Las Vegas please add "Brought To You By" (logo marlowe bright works or something...basically its a partnership with the Charity and Marlowe Bright Work)

So Marlowe Bright Work is a marketing company and not a Charity but more of a plug and play platform that allows a charity to accepts donations and immediately deliver the promised incentive offer after donation is made on the website.

When a Charity is able to offer a high perceived value gift for a donation they increase donations.

Target Market(s)

PEOPLE THAT DONATE TO CHARITIES

Industry/Entity Type

Charity

Number of Pages Required

3 page

Requirements
Must have
• One thing i need to add to the website is an Incentive Gift for the Donation.

So I need this tagline and images to make the promotion seem great:
"Donate $100 and Receive A Free 3 Night Vacation Certificate To Las Vegas!"

Maybe show image of vegas or some kind of nice graphic that promotes the vegas vacation as a gift for the $100 donation very well"

I need the payment pages as well. So when someone click Donate Now, the next page is there where they can see their gift that is included with the donation, and also the donation amount...
Nice to have

Should not have

```html
<!DOCTYPE html>
<html lang="en">
<head>
<meta charset="utf-8">
<title>Marlowe Bright Works – Charity Donation Template</title>
<link href="https://fonts.googleapis.com/css2?family=Montserrat:wght@600;700;800&family=Jost:wght@300;400;500&family=Oswald:wght@400&display=swap" rel="stylesheet">
<style>
:root{
  --orange:#f7860f;
  --orange-deep:#f27a0a;
  --ink:#2a2a2a;
  --body:#444;
  --muted:#777;
  --board:#a3a3a3;
  --hero:#0c0c10;
  --band:#eeeff1;
  --line:#e2e2e2;
  --chip:#e9e9ea;
  --slate:#555659;
  --white:#fff;
}
*{box-sizing:border-box;margin:0;padding:0}
html,body{width:1200px;height:2239px;overflow:hidden}
body{background:var(--board);position:relative;font-family:"Jost",sans-serif;color:var(--body)}
.abs{position:absolute}
.page{position:absolute;left:65px;top:32px;width:483px;height:2174px;background:var(--white);overflow:hidden}
.section{position:absolute;left:0;width:483px}
.logo-text{font-family:"Montserrat",sans-serif;font-weight:800;color:var(--orange);letter-spacing:.2px}
.btn{position:absolute;display:flex;align-items:center;justify-content:center;font-family:"Montserrat",sans-serif;font-weight:700;color:var(--white);background:var(--orange);border-radius:2px;letter-spacing:.3px}
.btn.dark{background:var(--slate)}
.photo{position:absolute;border-radius:2px}
.tag{position:absolute;background:var(--chip);font-size:7.5px;padding:2px 4px;color:#555;font-weight:400}
.kicker{position:absolute;font-family:"Montserrat",sans-serif;font-weight:800;color:var(--orange);font-size:7.5px}
.copy{position:absolute;font-size:6.8px;line-height:10.4px;color:#4a4a4a}
.copy p+p{margin-top:10px}
.stat-label{position:absolute;background:var(--chip);font-family:"Montserrat",sans-serif;font-weight:700;font-size:4.6px;text-align:center;padding:2px 0;color:#555}
.stat-value{position:absolute;font-family:"Montserrat",sans-serif;font-weight:600;font-size:5px;text-align:center;color:#444}
.header-bar{top:0;height:36px;border-bottom:1px solid #333}
.hero{top:37px;height:235px;background:var(--hero)}
.hero h1{position:absolute;left:36px;top:58px;font-family:"Montserrat",sans-serif;font-weight:800;font-size:25px;color:var(--white);letter-spacing:.3px}
.hero .sub{position:absolute;left:36px;top:91px;font-size:13px;line-height:17px;color:var(--white);font-weight:300}
.divider{position:absolute;background:var(--line)}
.brand{display:flex;align-items:center;gap:4px;font-family:"Montserrat",sans-serif;font-weight:700;color:var(--orange)}
.brand i{display:block;border-radius:50%;background:var(--orange)}
.number{position:absolute;font-family:"Montserrat",sans-serif;font-weight:700;color:#333}
.num-label{position:absolute;font-family:"Montserrat",sans-serif;font-weight:700;color:var(--orange)}
.quote-band{background:var(--band)}
.foot{background:var(--orange)}
.board-title{position:absolute;left:700px;top:24px;width:332px;text-align:center;font-family:"Oswald",sans-serif;font-size:42px;color:var(--white);letter-spacing:-.5px}
/* popup preview */
.preview{position:absolute;left:621px;top:465px;width:491px;height:847px;background:var(--white);overflow:hidden}
.shade{position:absolute;inset:0;background:rgba(40,40,40,.55)}
.popup{position:absolute;left:90px;top:202px;width:310px;height:349px;background:#f2f2f3;box-shadow:0 1px 4px rgba(0,0,0,.25)}
.popup-head{position:absolute;left:0;top:0;width:310px;height:34px;border-bottom:1px solid #d6d6d6;display:flex;align-items:center;padding-left:18px;font-family:"Montserrat",sans-serif;font-weight:700;font-size:10.5px;color:#333}
.close{position:absolute;right:14px;top:11px;width:15px;height:11px;background:#c9c9cb;border-radius:2px}
.field-label{position:absolute;font-size:8px;color:#333}
.field{position:absolute;height:19px;background:var(--white);border:1px solid #d9d9d9;font-size:7px;color:#888;padding-left:7px;display:flex;align-items:center}
.amount{position:absolute;left:18px;top:72px;width:113px;height:37px;background:var(--white);border:1px solid #d9d9d9;display:flex;align-items:center}
.amount b{width:26px;height:100%;display:flex;align-items:center;justify-content:center;font-size:20px;font-family:"Montserrat",sans-serif;color:#333;border-right:1px solid #d9d9d9}
.amount span{padding-left:7px;font-size:17px;font-family:"Montserrat",sans-serif;font-weight:600;color:#333}
.check{position:absolute;width:9px;height:9px;background:var(--white);border:1px solid #ccc}
.captcha{position:absolute;left:18px;top:297px;width:140px;height:37px;background:var(--white);border:1px solid #d3d3d3;border-radius:2px}
</style>
</head>
<body>

<!-- Landing page -->
<main class="page">

  <header class="section header-bar">
    <div class="abs logo-text" style="left:36px;top:12px;font-size:11.5px">LOGO HERE</div>
    <div class="btn" style="left:376px;top:10px;width:72px;height:17px;font-size:5.6px">BECOME A DONOR</div>
  </header>

  <section class="section hero">
    <h1>DONATE $100</h1>
    <div class="sub">GET A FREE 3 NIGHTS VACATION<br>CERTIFICATE FOR LAS VEGAS!</div>
    <div class="btn" style="left:36px;top:128px;width:72px;height:16px;font-size:5.8px">DONATE TODAY</div>
    <div class="photo" role="img" aria-label="Illuminated Welcome to Las Vegas sign at night" style="left:256px;top:22px;width:200px;height:160px;background:radial-gradient(ellipse at 55% 55%,#3f6fc4 0%,#1c3a7a 35%,#a31d2a 52%,#0c0c10 72%)"></div>
  </section>

  <section class="section" style="top:272px;height:204px;border-bottom:1px solid var(--line)">
    <div class="photo" role="img" aria-label="Las Vegas strip skyline at dusk" style="left:36px;top:21px;width:180px;height:131px;background:linear-gradient(180deg,#2c3f8e 0%,#6c5a9a 35%,#c7814a 58%,#3b2a1e 80%,#16110c 100%)"></div>
    <div class="abs" style="left:43px;top:139px;font-family:Montserrat,sans-serif;font-weight:700;font-size:5.3px;color:#fff">3 NIGHTS VACATION CERTIFICATE FOR LAS VEGAS!</div>
    <div class="abs" style="left:40px;top:166px;font-size:4.8px;font-weight:500;color:#333">Brought To You By:</div>
    <div class="abs brand" style="left:92px;top:160px;font-size:10px"><i style="width:12px;height:12px"></i>Marlowe Bright Works</div>
    <div class="divider" style="left:242px;top:0;width:1px;height:204px"></div>
    <div class="copy" style="left:285px;top:22px;width:165px;font-size:6.6px;line-height:10px">Donate today &amp; help us reach our $1M goal to Lorem Ipsum is simply dummy text of the printing</div>
    <div class="btn" style="left:327px;top:51px;width:72px;height:15px;font-size:5.8px">DONATE NOW</div>
    <div class="btn dark" style="left:327px;top:72px;width:72px;height:15px;font-size:5.8px">SHARE</div>
    <div class="number" style="left:285px;top:93px;font-size:19px">350</div>
    <div class="num-label" style="left:285px;top:118px;font-size:7px">DONORS</div>
    <div class="number" style="left:285px;top:124px;font-size:19px">$200,728</div>
    <div class="num-label" style="left:285px;top:149px;font-size:7px">RAISED (USD)</div>
    <div class="abs" style="left:285px;top:165px;width:155px;height:5px;border:1px solid #ddd;border-radius:3px"><div style="width:52px;height:3px;background:var(--orange);border-radius:3px"></div></div>
    <div class="abs" style="left:285px;top:173px;font-family:Montserrat,sans-serif;font-weight:700;font-size:4.5px;color:#333">Goal: <span style="color:var(--orange)">$1 000 000</span></div>
    <div class="abs" style="left:410px;top:173px;font-family:Montserrat,sans-serif;font-weight:700;font-size:4.5px;color:#333">Days Left: <span style="color:var(--orange)">26</span></div>
  </section>

  <section class="section" style="top:476px;height:291px;border-bottom:1px solid var(--line)">
    <div class="tag" style="left:36px;top:31px">THE FACTS</div>
    <div class="kicker" style="left:36px;top:53px">PERSPICIATIS UNDE OMNIS</div>
    <div class="copy" style="left:36px;top:69px;width:160px">
      <p>Lorem ipsum dolor sit amet, consectetur adipisicing elit, sed do eiusmod tempor incididunt ut labore et dolore magna aliqua. Ut enim ad minim veniam. Duis aute irure dolor in reprehenderit in voluptate velit esse cillum dolore eu fugiat nulla pariatur. Excepteur sint occaecat cupidatat non proident.</p>
      <p>Lorem ipsum dolor sit amet, consectetur adipisicing elit, sed do eiusmod tempor incididunt ut labore et dolore magna aliqua. Ut enim ad minim veniam, quis nostrud exercitation ullamco laboris nisi ut aliquip ex ea commodo consequat.</p>
    </div>
    <div class="photo" role="img" aria-label="Giant panda sitting on rocks" style="left:256px;top:24px;width:193px;height:165px;background:linear-gradient(160deg,#6b6a63 0%,#3c3b37 45%,#a19c8f 75%,#5a5650 100%)"></div>
    <div class="abs" style="left:256px;top:193px;width:193px;text-align:center;font-size:7.5px;color:#444">CONSERVATION STATUS</div>
    <div class="abs" style="left:256px;top:205px;width:193px;text-align:center;font-size:7.5px;color:var(--orange)">Vulnerable</div>
    <div class="stat-label" style="left:278px;top:222px;width:59px">EST POPULATION</div>
    <div class="stat-value" style="left:273px;top:234px;width:69px">10,000-15,000</div>
    <div class="stat-label" style="left:368px;top:222px;width:59px">LIFESPAN</div>
    <div class="stat-value" style="left:363px;top:234px;width:69px">30-50 years</div>
    <div class="stat-label" style="left:278px;top:252px;width:59px">WEIGHT</div>
    <div class="stat-value" style="left:273px;top:264px;width:69px">210-520kg</div>
    <div class="stat-label" style="left:368px;top:252px;width:59px">SCIENTIFIC NAME</div>
    <div class="stat-value" style="left:353px;top:264px;width:89px">Ailuropoda melanoleuca</div>
  </section>

  <section class="section" style="top:767px;height:230px;border-bottom:1px solid var(--line)">
    <div class="photo" role="img" aria-label="Giant panda eating bamboo" style="left:36px;top:18px;width:193px;height:165px;background:linear-gradient(150deg,#8a7a5e 0%,#4f4636 50%,#9c8c6c 100%)"></div>
    <div class="tag" style="left:295px;top:27px">THE ISSUES</div>
    <div class="kicker" style="left:295px;top:48px">PERSPICIATIS UNDE OMNIS</div>
    <div class="copy" style="left:295px;top:64px;width:155px">
      <p>Lorem ipsum dolor sit amet, consectetur adipisicing elit, sed do eiusmod tempor incididunt ut labore et dolore magna aliqua. Ut enim ad minim veniam. Duis aute irure dolor in reprehenderit in voluptate velit esse cillum dolore eu fugiat nulla pariatur. Excepteur sint occaecat cupidatat non proident.</p>
      <p>Lorem ipsum dolor sit amet, consectetur adipisicing elit, sed do eiusmod tempor incididunt ut labore et dolore magna aliqua. Ut enim ad minim veniam, quis nostrud exercitation ullamco laboris nisi ut aliquip ex ea commodo consequat.</p>
    </div>
  </section>

  <section class="section" style="top:997px;height:229px">
    <div class="tag" style="left:36px;top:27px">THE URGENCY</div>
    <div class="kicker" style="left:36px;top:48px">PERSPICIATIS UNDE OMNIS</div>
    <div class="copy" style="left:36px;top:64px;width:160px">
      <p>Lorem ipsum dolor sit amet, consectetur adipisicing elit, sed do eiusmod tempor incididunt ut labore et dolore magna aliqua. Ut enim ad minim veniam. Duis aute irure dolor in reprehenderit in voluptate velit esse cillum dolore eu fugiat nulla pariatur. Excepteur sint occaecat cupidatat non proident.</p>
      <p>Lorem ipsum dolor sit amet, consectetur adipisicing elit, sed do eiusmod tempor incididunt ut labore et dolore magna aliqua. Ut enim ad minim veniam, quis nostrud exercitation ullamco laboris nisi ut aliquip ex ea commodo consequat.</p>
    </div>
    <div class="photo" role="img" aria-label="Black and white photo of a panda among bamboo" style="left:256px;top:17px;width:193px;height:165px;background:linear-gradient(160deg,#9a9a9a 0%,#4a4a4a 50%,#b5b5b5 100%)"></div>
  </section>

  <section class="section quote-band" style="top:1226px;height:115px">
    <div class="abs" style="left:60px;top:13px;width:363px;text-align:center;font-family:Montserrat,sans-serif;font-weight:700;font-size:5.6px;line-height:8.3px;color:#333">"Lorem ipsum dolor sit amet, consectetur adipisicing elit, sed do eiusmod tempor incididunt ut labore et dolore magna aliqua. Ut enim ad minim veniam. Duis aute irure dolor in reprehenderit in voluptate velit esse cillum dolore eu fugiat nulla pariatur. Excepteur sint occaecat cupidatat non proident."</div>
    <div class="abs" style="left:0;top:42px;width:483px;text-align:center;font-size:7px;color:var(--orange)">Helena Dorsay</div>
    <div class="abs" style="left:0;top:52px;width:483px;text-align:center;font-size:5.8px;color:#444">CO-FOUNDER OF PANDA TRUST</div>
    <div class="abs" style="left:45px;top:46px;font-size:12px;color:#444">«</div>
    <div class="abs" style="left:430px;top:46px;font-size:12px;color:#444">»</div>
    <div class="abs" role="img" aria-label="Portrait of the co-founder" style="left:232px;top:62px;width:19px;height:19px;border-radius:50%;background:linear-gradient(#e9b48c,#c9855a)"></div>
    <div class="btn" style="left:206px;top:87px;width:72px;height:16px;font-size:5.8px">DONATE NOW</div>
    <svg class="abs" style="left:233px;top:115px" width="18" height="10" viewBox="0 0 18 10"><path d="M0 0 L9 10 L18 0 Z" fill="#eeeff1"/></svg>
  </section>

  <section class="section" style="top:1341px;height:720px">
    <div class="tag" style="left:78px;top:23px">THE SOLUTION</div>
    <div class="kicker" style="left:78px;top:44px">PERSPICIATIS UNDE OMNIS</div>
    <div class="copy" style="left:78px;top:60px;width:325px">Lorem ipsum dolor sit amet, consectetur adipisicing elit, sed do eiusmod tempor incididunt ut labore et dolore magna aliqua. Ut enim ad minim veniam. Duis aute irure dolor in reprehenderit in voluptate velit esse cillum dolore eu fugiat nulla pariatur. Excepteur sint occaecat cupidatat non proident.</div>
    <div class="photo" role="img" aria-label="Video still of a panda climbing a tree in a forest" style="left:80px;top:107px;width:343px;height:193px;border-radius:0;background:linear-gradient(160deg,#6f7a3a 0%,#3e4a22 45%,#8a8444 75%,#4d5628 100%)"></div>
    <svg class="abs" style="left:231px;top:183px" width="40" height="40" viewBox="0 0 40 40"><circle cx="20" cy="20" r="19" fill="none" stroke="#fff" stroke-width="1.3"/><path d="M16 12 L29 20 L16 28 Z" fill="#fff"/></svg>

    <div class="photo" role="img" aria-label="Panda resting on a tree branch" style="left:80px;top:328px;width:112px;height:95px;background:linear-gradient(150deg,#5f7a3c,#3a3a30 60%,#7b6a4c)"></div>
    <div class="kicker" style="left:210px;top:331px">PERSPICIATIS UNDE OMNIS</div>
    <div class="copy" style="left:210px;top:347px;width:205px">Lorem ipsum dolor sit amet, consectetur adipisicing elit, sed do eiusmod tempor incididunt ut labore et dolore magna aliqua. Ut enim ad minim veniam. Duis aute irure dolor in reprehenderit in voluptate velit esse cillum dolore eu fugiat nulla pariatur. Excepteur sint occaecat cupidatat non proident.</div>

    <div class="kicker" style="left:80px;top:451px">PERSPICIATIS UNDE OMNIS</div>
    <div class="copy" style="left:80px;top:467px;width:205px">Lorem ipsum dolor sit amet, consectetur adipisicing elit, sed do eiusmod tempor incididunt ut labore et dolore magna aliqua. Ut enim ad minim veniam. Duis aute irure dolor in reprehenderit in voluptate velit esse cillum dolore eu fugiat nulla pariatur. Excepteur sint occaecat cupidatat non proident.</div>
    <div class="photo" role="img" aria-label="Panda eating bamboo shoots" style="left:311px;top:448px;width:112px;height:95px;background:linear-gradient(150deg,#7a6c52,#3a342a 60%,#9a8866)"></div>

    <div class="photo" role="img" aria-label="Panda sitting among bamboo stalks" style="left:80px;top:568px;width:112px;height:95px;background:linear-gradient(150deg,#4e6a34,#2f3a26 60%,#77804c)"></div>
    <div class="kicker" style="left:210px;top:571px">PERSPICIATIS UNDE OMNIS</div>
    <div class="copy" style="left:210px;top:587px;width:205px">Lorem ipsum dolor sit amet, consectetur adipisicing elit, sed do eiusmod tempor incididunt ut labore et dolore magna aliqua. Ut enim ad minim veniam. Duis aute irure dolor in reprehenderit in voluptate velit esse cillum dolore eu fugiat nulla pariatur. Excepteur sint occaecat cupidatat non proident.</div>
  </section>

  <section class="section foot" style="top:2061px;height:113px">
    <div class="abs" style="left:0;top:33px;width:483px;text-align:center;font-family:Montserrat,sans-serif;font-weight:700;font-size:13.5px;line-height:18px;color:#fff">Donate today &amp; help us reach our $1M goal to<br>Lorem Ipsum is simply dummy text of the</div>
    <div class="btn dark" style="left:206px;top:83px;width:72px;height:15px;font-size:5.8px;background:#3a3a3c">DONATE NOW</div>
  </section>
</main>

<div class="board-title">Donation pop up.</div>

<!-- Donation pop-up over the page -->
<section class="preview" aria-label="Donation pop-up">
  <div class="abs" style="left:0;top:0;width:491px;height:36px;background:#fff;border-bottom:1px solid #333"></div>
  <div class="abs logo-text" style="left:36px;top:12px;font-size:11.5px">LOGO HERE</div>
  <div class="btn" style="left:380px;top:10px;width:73px;height:17px;font-size:5.6px">BECOME A DONOR</div>
  <div class="abs" style="left:0;top:37px;width:491px;height:239px;background:var(--hero)"></div>
  <div class="abs" style="left:36px;top:95px;font-family:Montserrat,sans-serif;font-weight:800;font-size:25px;color:#fff">DONATE $100</div>
  <div class="abs" style="left:36px;top:128px;font-size:13px;line-height:17px;color:#fff;font-weight:300">GET A FREE 3 NIGHTS VACATION<br>CERTIFICATE FOR LAS VEGAS!</div>
  <div class="btn" style="left:36px;top:166px;width:73px;height:16px;font-size:5.8px">DONATE TODAY</div>
  <div class="photo" role="img" aria-label="Illuminated Welcome to Las Vegas sign at night" style="left:262px;top:58px;width:204px;height:160px;background:radial-gradient(ellipse at 55% 55%,#3f6fc4 0%,#1c3a7a 35%,#a31d2a 52%,#0c0c10 72%)"></div>
  <div class="photo" role="img" aria-label="Las Vegas strip skyline at dusk" style="left:36px;top:297px;width:183px;height:133px;background:linear-gradient(180deg,#2c3f8e 0%,#6c5a9a 35%,#c7814a 58%,#16110c 100%)"></div>
  <div class="abs" style="left:41px;top:414px;font-family:Montserrat,sans-serif;font-weight:700;font-size:5.3px;color:#fff">3 NIGHTS VACATION CERTIFICATE FOR LAS VEGAS!</div>
  <div class="abs" style="left:40px;top:449px;font-size:4.8px;font-weight:500;color:#333">Brought To You By:</div>
  <div class="tag" style="left:36px;top:518px">THE FACTS</div>
  <div class="kicker" style="left:36px;top:540px">PERSPICIATIS UNDE OMNIS</div>
  <div class="copy" style="left:36px;top:556px;width:163px">
    <p>Lorem ipsum dolor sit amet, consectetur adipisicing elit, sed do eiusmod tempor incididunt ut labore et dolore magna aliqua. Ut enim ad minim veniam. Duis aute irure dolor in reprehenderit in voluptate velit esse cillum dolore eu fugiat nulla pariatur. Excepteur sint occaecat cupidatat non proident.</p>
    <p>Lorem ipsum dolor sit amet, consectetur adipisicing elit, sed do eiusmod tempor incididunt ut labore et dolore magna aliqua. Ut enim ad minim veniam, quis nostrud exercitation ullamco laboris nisi ut aliquip ex ea commodo consequat.</p>
  </div>
  <div class="photo" role="img" aria-label="Giant panda sitting on rocks" style="left:260px;top:507px;width:196px;height:167px;background:linear-gradient(160deg,#6b6a63 0%,#3c3b37 45%,#a19c8f 75%,#5a5650 100%)"></div>
  <div class="abs" style="left:260px;top:682px;width:196px;text-align:center;font-size:7.5px;color:#444">CONSERVATION STATUS</div>
  <div class="abs" style="left:260px;top:694px;width:196px;text-align:center;font-size:7.5px;color:var(--orange)">Vulnerable</div>
  <div class="stat-label" style="left:282px;top:711px;width:60px">EST POPULATION</div>
  <div class="stat-value" style="left:277px;top:723px;width:70px">10,000-15,000</div>
  <div class="stat-label" style="left:374px;top:711px;width:60px">LIFESPAN</div>
  <div class="stat-value" style="left:369px;top:723px;width:70px">30-50 years</div>
  <div class="stat-label" style="left:282px;top:741px;width:60px">WEIGHT</div>
  <div class="stat-value" style="left:277px;top:753px;width:70px">210-520kg</div>
  <div class="stat-label" style="left:374px;top:741px;width:60px">SCIENTIFIC NAME</div>
  <div class="stat-value" style="left:359px;top:753px;width:90px">Ailuropoda melanoleuca</div>
  <div class="photo" role="img" aria-label="Giant panda eating bamboo" style="left:36px;top:797px;width:196px;height:60px;background:linear-gradient(150deg,#8a7a5e,#4f4636)"></div>
  <div class="tag" style="left:300px;top:806px">THE ISSUES</div>
  <div class="kicker" style="left:300px;top:827px">PERSPICIATIS UNDE OMNIS</div>
  <div class="shade"></div>

  <div class="popup" role="dialog" aria-label="Your Donation Will Make A Difference">
    <div class="popup-head">Your Donation Will Make A Difference</div>
    <div class="close"><svg width="15" height="11" viewBox="0 0 15 11"><path d="M5 3 L10 8 M10 3 L5 8" stroke="#fff" stroke-width="1.3"/></svg></div>

    <div class="field-label" style="left:18px;top:57px">ENTER YOUR AMOUNT:</div>
    <div class="amount"><b>$</b><span>100</span></div>
    <div class="field-label" style="left:18px;top:115px">DONATIONS IN USD</div>
    <div class="field-label" style="left:18px;top:148px">DONATING TO:</div>
    <div class="abs logo-text" style="left:18px;top:162px;font-size:19px;line-height:27px">LOGO<br>&nbsp;HERE</div>
    <div class="check" style="left:18px;top:225px"></div>
    <div class="field-label" style="left:32px;top:224px">Contribute Each Month</div>

    <div class="field-label" style="left:161px;top:57px">YOUR DETAILS:</div>
    <div class="field" style="left:161px;top:73px;width:116px">First &amp; Last Name</div>
    <div class="abs" style="left:277px;top:73px;width:17px;height:19px;background:#fff;border:1px solid #d9d9d9;display:flex;align-items:center;justify-content:center"><i style="display:block;width:7px;height:7px;background:#3b5a98"></i></div>
    <div class="field" style="left:161px;top:98px;width:133px">Email</div>
    <div class="field" style="left:161px;top:123px;width:133px">Billing Address</div>
    <div class="field" style="left:161px;top:148px;width:47px">Zip Code</div>
    <div class="field" style="left:161px;top:173px;width:133px">Credit Card Number</div>
    <div class="field" style="left:161px;top:198px;width:38px">Month</div>
    <div class="field" style="left:208px;top:198px;width:38px">Year</div>
    <div class="field" style="left:256px;top:198px;width:38px">CVV</div>
    <div class="field" style="left:161px;top:222px;width:133px;height:48px;align-items:flex-start;padding-top:5px">Add message</div>

    <div class="abs" style="left:0;top:287px;width:310px;height:1px;background:#d6d6d6"></div>
    <div class="captcha">
      <div class="check" style="left:8px;top:13px;width:11px;height:11px"></div>
      <div class="abs" style="left:25px;top:13px;font-size:6.2px;color:#333">Je ne suis pas un robot</div>
      <div class="abs" style="left:114px;top:5px;width:12px;height:12px;background:#4a7fd6;border-radius:2px"></div>
      <div class="abs" style="left:104px;top:20px;font-size:4.5px;color:#666">CheckGate</div>
      <div class="abs" style="left:98px;top:27px;font-size:3.8px;color:#888">Privacy - Terms</div>
    </div>
    <div class="btn" style="left:172px;top:303px;width:116px;height:22px;font-size:7.6px;background:var(--orange-deep)">MAKE YOUR DONATION</div>
  </div>
</section>

</body>
</html>
```